Website Re-design

Hi, I'm looking for help in redesigning my web site. I currently have a site www.brightmoorlamps.example where I sell lamps, and while I like some aspects of the design, you can tell that I have done the graphics myself and am not a pro at it. I'd like help in redesigning it, and am open to completely new design graphics. I have made the 3 slider images myself, and I feel they could be a bit better, but I am not sure how to do it. For example, on the homepage, the 'About Us', 'Secured Shopping', and '$10 Off' graphics don't go well with the rest of the page. I would like more cohesion in the design and more visual interest in the header, which is pretty basic right now. Also, that the bottom footer is black, I would like instead something else. I am looking for just the layout of the homepage, and possibly once that is done to work on more visual interest in some of the informational pages and product pages. I am looking for just the design in the form of a photoshop file or files that I can incorporate into my site. Thank you!
Updates

Project Deadline Extended
Reason: I just made this project payment committed, so I'd like a chance for designers who only choose payment committed projects to submit artwork. Thank you.

This project is now payment guaranteed/ committed.  Thanks.

Industry/Entity Type

Shopping

```html
<!DOCTYPE html>
<html lang="en">
<head>
<meta charset="utf-8">
<title>Brightmoor Lamps – Home</title>
<link rel="stylesheet" href="https://fonts.googleapis.com/css2?family=Raleway:wght@300;400;500;600;700&family=Pacifico&display=swap">
<style>
  :root {
    --accent: #f0134d;
    --ink: #333333;
    --ink-soft: #555555;
    --teal: #2a9d99;
    --teal-ring: #8ccfcc;
    --pink: #e8184f;
    --pink-ring: #f58fa6;
    --orange: #f39c1b;
    --orange-ring: #f8cd80;
    --footer: #2b2b2b;
    --footer-line: #3a3a3a;
    --white: #ffffff;
  }
  * { margin: 0; padding: 0; box-sizing: border-box; }
  html, body { width: 857px; height: 1200px; overflow: hidden; }
  body {
    position: relative;
    background: var(--white);
    font-family: "Raleway", Arial, sans-serif;
    color: var(--ink);
  }
  .abs { position: absolute; }

  /* Header */
  .login-label { left: 245px; top: 14px; font-size: 11px; }
  .field {
    height: 14px; background: #e6e6e6; border: 1px solid #bdbdbd;
    font-size: 7px; color: #9a9a9a; padding-left: 5px; line-height: 12px;
  }
  .field-email { left: 333px; top: 14px; width: 71px; }
  .field-pass { left: 420px; top: 14px; width: 70px; }
  .login-btn {
    left: 504px; top: 14px; width: 48px; height: 14px; background: var(--accent);
    color: var(--white); font-size: 10px; font-weight: 700; text-align: center; line-height: 14px;
  }
  .cart { left: 627px; top: 10px; }
  .cart-count { left: 657px; top: 14px; font-size: 11px; }
  .cart-price { left: 718px; top: 14px; font-size: 11px; }
  .cart-count span, .cart-price span { color: var(--accent); }

  .brand {
    left: 80px; top: 26px; display: flex; align-items: center; gap: 8px;
  }
  .brand-mark { width: 40px; height: 40px; border: 2px solid #4a4a4a; border-radius: 50%; }
  .brand-name { font-size: 19px; font-weight: 600; color: #4a4a4a; line-height: 21px; }

  .nav { left: 268px; top: 55px; display: flex; gap: 0; font-size: 14px; }
  .nav a { color: var(--ink); text-decoration: none; position: absolute; white-space: nowrap; }

  .search {
    left: 594px; top: 53px; width: 178px; height: 21px; border-radius: 11px;
    background: linear-gradient(#f2f2f2, #d9d9d9); border: 1px solid #c8c8c8;
    font-size: 8px; color: #999; padding-left: 18px; line-height: 19px;
  }
  .search-btn {
    left: 750px; top: 52px; width: 23px; height: 23px; border-radius: 50%; background: var(--teal);
  }

  /* Hero */
  .hero {
    left: 73px; top: 90px; width: 712px; height: 382px;
    background: linear-gradient(180deg, #4fb0b4 0%, #7fd0d2 55%, #a8e2e1 72%, #cfd3d2 73%, #b9bdbc 100%);
    box-shadow: 0 14px 18px -10px rgba(0,0,0,.35);
  }
  .hero-title {
    left: 165px; top: 128px; font-family: "Pacifico", cursive; font-size: 46px;
    line-height: 74px; color: var(--white); text-shadow: 0 2px 4px rgba(0,0,0,.2);
  }
  .hero-sub { left: 145px; top: 292px; font-size: 18px; color: var(--white); letter-spacing: .5px; }
  .hero-btn {
    left: 150px; top: 356px; width: 148px; height: 31px; background: var(--accent);
    color: var(--white); font-size: 18px; text-align: center; line-height: 31px;
  }
  .dots { left: 403px; top: 489px; }

  /* Features */
  .feature { top: 563px; width: 230px; text-align: center; }
  .feature-icon { width: 116px; height: 116px; margin: 0 auto; }
  .feature h2 { font-size: 22px; font-weight: 400; color: var(--ink-soft); margin-top: 13px; }
  .feature p { font-size: 11px; line-height: 14.5px; color: #444; width: 165px; margin: 14px auto 0; }
  .read-more {
    position: absolute; top: 246px; left: 81px; width: 68px; height: 22px; background: var(--accent);
    color: var(--white); font-size: 10px; font-weight: 700; line-height: 22px; text-align: center;
  }
  .divider { left: 0; top: 950px; width: 857px; height: 1px; background: #ececec; }

  /* Footer */
  .footer { left: 0; top: 997px; width: 857px; height: 203px; background: var(--footer); border-top: 3px solid #1e1e1e; }
  .footer-col { top: 1009px; color: var(--white); }
  .footer-col h3 { font-size: 18px; font-weight: 400; margin-bottom: 10px; }
  .footer-col ul { list-style: none; font-size: 11px; line-height: 14.5px; padding-left: 2px; }
  .social { top: 1138px; width: 30px; height: 30px; border-radius: 5px; }
  .newsletter-title { left: 465px; top: 1103px; font-size: 21px; color: var(--white); font-weight: 400; }
  .newsletter-input {
    left: 466px; top: 1136px; width: 207px; height: 24px; border: 1px solid #b01238;
    color: var(--white); font-size: 14px; padding-left: 11px; line-height: 22px;
  }
  .newsletter-btn {
    left: 692px; top: 1133px; width: 87px; height: 28px; background: var(--accent);
    color: var(--white); font-size: 13px; font-weight: 700; text-align: center; line-height: 28px;
  }
  .copyright { left: 0; top: 1189px; width: 888px; text-align: center; color: var(--white); font-size: 8px; }
</style>
</head>
<body>
  <header>
    <div class="abs login-label">Login / Register</div>
    <div class="abs field field-email">Email</div>
    <div class="abs field field-pass">password</div>
    <div class="abs login-btn">Login</div>

    <svg class="abs cart" width="26" height="20" viewBox="0 0 26 20" aria-hidden="true">
      <path d="M1 2h5l3 11h12l3-8H8" fill="none" stroke="#f0134d" stroke-width="2"/>
      <circle cx="11" cy="17" r="2" fill="#f0134d"/><circle cx="20" cy="17" r="2" fill="#f0134d"/>
    </svg>
    <div class="abs cart-count">product <span>0</span></div>
    <div class="abs cart-price">price <span>$0.00</span></div>

    <div class="abs brand">
      <div class="brand-mark"></div>
      <div class="brand-name">brightmoor<br>lamps</div>
    </div>

    <nav class="abs nav">
      <a style="left:0">HOME</a>
      <a style="left:58px">SHOP</a>
      <a style="left:113px">ABOUT US</a>
      <a style="left:199px">CONTACT US</a>
    </nav>

    <div class="abs search">Search</div>
    <div class="abs search-btn"></div>
  </header>

  <section>
    <div class="abs hero" role="img" aria-label="Glass table lamp with white shade on a pale wooden floor against a teal wall"></div>
    <div class="abs hero-title">Light Up<br>The Room</div>
    <div class="abs hero-sub">“The Lagoon” Medium table lampe</div>
    <div class="abs hero-btn">Go shop</div>
    <svg class="abs dots" width="62" height="14" viewBox="0 0 62 14" aria-hidden="true">
      <circle cx="3" cy="7" r="3" fill="#2a9d99"/><circle cx="16" cy="7" r="3" fill="#2a9d99"/>
      <circle cx="30" cy="7" r="5" fill="none" stroke="#2a9d99" stroke-width="2"/>
      <circle cx="44" cy="7" r="3" fill="#2a9d99"/><circle cx="57" cy="7" r="3" fill="#2a9d99"/>
    </svg>
  </section>

  <section>
    <div class="abs feature" style="left:45px">
      <svg class="feature-icon" viewBox="0 0 116 116" aria-hidden="true">
        <circle cx="58" cy="58" r="58" fill="var(--teal-ring)"/><circle cx="58" cy="58" r="47" fill="var(--teal)"/>
        <g fill="none" stroke="#fff" stroke-width="3" stroke-linejoin="round">
          <path d="M46 34h24l8 20H38z"/><path d="M53 54c-10 8-6 24 5 24s15-16 5-24"/><path d="M48 84h20"/>
        </g>
      </svg>
      <h2>About Us</h2>
      <p>Brightmoor Lamps provides beauti-ful and artistic home and hospitality lighting.</p>
      <div class="read-more">READ MORE</div>
    </div>

    <div class="abs feature" style="left:314px">
      <svg class="feature-icon" viewBox="0 0 116 116" aria-hidden="true">
        <circle cx="58" cy="58" r="58" fill="var(--pink-ring)"/><circle cx="58" cy="58" r="47" fill="var(--pink)"/>
        <g fill="none" stroke="#fff" stroke-width="3" stroke-linejoin="round">
          <path d="M40 46l12-12M76 46L64 34"/><rect x="32" y="46" width="52" height="8"/>
          <path d="M36 54l4 20h36l4-20"/><path d="M48 58v12M58 58v12M68 58v12"/>
        </g>
      </svg>
      <h2>Secure Shopping</h2>
      <p>Shopping at Brightmoor Lamps is secured and protected by industry standard best practices and hospitality lighting.</p>
      <div class="read-more">READ MORE</div>
    </div>

    <div class="abs feature" style="left:583px">
      <svg class="feature-icon" viewBox="0 0 116 116" aria-hidden="true">
        <circle cx="58" cy="58" r="58" fill="var(--orange-ring)"/><circle cx="58" cy="58" r="47" fill="var(--orange)"/>
        <g fill="none" stroke="#fff" stroke-width="3" stroke-linejoin="round">
          <path d="M48 70c0-8-8-12-8-22a18 18 0 0 1 36 0c0 10-8 14-8 22z"/>
          <path d="M50 76h16M52 82h12"/><path d="M54 70V56l4 4 4-4v14"/>
        </g>
      </svg>
      <h2>To The Trade</h2>
      <p>We are pleased to offer interior decorators, designers, and architects 10% off on all online merchandise at Brightmoor Lamps.</p>
      <div class="read-more">READ MORE</div>
    </div>
  </section>

  <div class="abs divider"></div>

  <footer>
    <div class="abs footer"></div>
    <div class="abs footer-col" style="left:90px">
      <h3>Help + Info</h3>
      <ul><li>Contact Us</li><li>Shipping Info</li><li>Returns</li><li>To The Trade</li><li>Privacy Policy</li><li>Terms of Use</li></ul>
    </div>
    <div class="abs footer-col" style="left:278px">
      <h3>My Account</h3>
      <ul><li>Sign In</li><li>Order Status</li><li>Order History</li><li>View Cart</li><li>Checkout</li></ul>
    </div>
    <div class="abs footer-col" style="left:471px">
      <h3>About</h3>
      <ul><li>Who We Are</li><li>Testimonials</li></ul>
    </div>
    <div class="abs footer-col" style="left:666px; top:1006px">
      <h3>Contact</h3>
      <ul><li>Contact Us</li><li>info@brightmoorlamps.example</li></ul>
    </div>

    <div class="abs social" style="left:252px; background:#3b5998"></div>
    <div class="abs social" style="left:295px; background:#55c5e6"></div>
    <div class="abs social" style="left:337px; background:#cb2027"></div>

    <div class="abs newsletter-title">Newsletter</div>
    <div class="abs newsletter-input">E-mail address</div>
    <div class="abs newsletter-btn">Submit</div>

    <div class="abs copyright">© Brightmoor Lamps 2013 | All Rights Reserved</div>
  </footer>
</body>
</html>
```